Vigorhaven home exercise studio needs a brochure design

My problem is that I have had a fitness studio within my home for 3 years and only 2 clients per week to show for it! I need a fitness brochure designed that will literally want to make a customer pick up the phone and book a training session!

If there is any way possible to convince those exercise lovers or those who wish to become active and healthy who want to train in a private home exercise studio setting than I will be very content and happy. Obviosuly my studio within my home is not exposed to the general public and I understand that this is the reason for a shortage of clients.

I have an exercise studio with my home. It is literally the size of 6-7 x area of a standard bedroom. Most importantly, it contains the latest state of the art exercise equipment (treamills, rowers, cycle & recumberant bikes, elastic cords, bands, medballs, resistance machines, cables, squat racks, you name it..

In addition, compared to many other personal trainers out within the industry, I have clearly distinguished myself from the rest in a positive way. Firstly, I have had an extensive background as an elite athlete (NSW wrestling representitive), secondly I have acquired a solid foundation of exercise science principles through 4 years of university studies (compared to most other trainers out there). Because my studio is private and obviously lacks many elements that a typical gym setting such as peak motion, then we must be able to highlight the positives that arise from my studio compared to peak motion or any other franchise (eg: no cancellation pollicies, no signing up for contracts, no membership fees). in addition, we must hihglight the fact that a private studio like mine will attract those who prefer not to train around others they do not know as there is no sharing of exercise equipment or duration of time one must be on a certain exercise.

We all know someone who prefers not to train in a typical gym setting where people have to compete against others for the equipment yet alone deal with the amount of starring and chatter that goes on. In addition it can get intimidating for those who prefer not many people around them. My studio is designed for any age or fitness category. In addition group training is avaliable.
In addition, I am flexible and sometimes permit going overtime for those clients who were late for there appointment. Clients that come to my home to exercise feel as if they are training within there own home rather than feeling the intimidation of going into a gym setting such as peak motion.

If we can highlight all that has been mentioned within my brochure than thats great!

Target Market(s)

I design exercise programs and train all age groups and fitness levels

Industry/Entity Type

University

Requirements
Must have
• There must be a quote in the brochure that mentions "Together,the sky is our limit"

Must have "vigorhaven" logo

must have testimonials:

Colin -"My golf drive has increased dramatically from the use of sports specific exercises that Howard was able to deliver. The pain in my lower back has now ceased to flare up after a game"

Miriam - "Howard's knowledge and application of exercise science and health has helped me achieve a stronger and leaner body in addition to improving my 5km walking time"

Must have my qualifications:
Certificate 4 personal trainer
Diploma of fitness
Bachelor of exercise and sport science
Diploma of remedial massage
First Aid certificate

Must state that I am registered with Active Registry Australia

Must have that I Specialize in:

1. exercise rehabilitation
2. sport specific conditioning
3. Functional strength
4. Fat loss and toning
5. Core strength & stability
6. Flexibility
7. Cardio-respiratory fitness

Must have my mobile number: 0427 586 903
Must have my email adress: hwtrelford@quillmail.com.au
Nice to have
• any background images that represent motivation, will and determination.

```html
<!DOCTYPE html>
<html lang="en">
<head>
<meta charset="utf-8">
<title>Vigorhaven – Home Exercise Studio Brochure</title>
<link rel="stylesheet" href="https://fonts.googleapis.com/css2?family=Gochi+Hand&family=Open+Sans:ital,wght@0,400;0,600;0,700;1,400&family=Playfair+Display+SC:wght@700&family=PT+Sans:wght@700&display=swap">
<style>
  :root {
    --orange: #ee7307;
    --white: #ffffff;
    --sky: #5baeea;
    --slate: #4a4f57;
    --lemon: #eef39a;
    --lemon-shadow: #6f6a3c;
    --bullet: #f2ea3c;
    --logo-grey: #a3a3a3;
    --ink: #111111;
    --veil: rgba(214, 178, 60, 0.62);
    --veil-band: rgba(40, 70, 150, 0.75);
    --sand-veil: rgba(238, 115, 7, 0.82);
  }
  * { box-sizing: border-box; margin: 0; padding: 0; }
  html, body { width: 1200px; height: 927px; overflow: hidden; background: var(--white); }
  .brochure { position: relative; width: 1200px; height: 927px; background: var(--white); }

  /* Testimonials panel */
  .testimonials {
    position: absolute; left: 12px; top: 12px; width: 388px; height: 903px;
    background: var(--orange); overflow: hidden;
  }
  .testimonials__title {
    font-family: "Gochi Hand", cursive; font-weight: 400; color: var(--white);
    font-size: 50px; text-align: center; margin-top: 14px; letter-spacing: 1px;
  }
  .quote {
    font-family: "Open Sans", sans-serif; font-style: italic; font-size: 16.5px;
    letter-spacing: 0.45px; line-height: 22.5px; color: var(--ink); padding: 0 26px 0 18px;
  }
  .quote--first { margin-top: 14px; }
  .quote--second { margin-top: 12px; }
  .quote__author {
    font-family: "Open Sans", sans-serif; font-weight: 600; font-size: 16.5px; color: var(--ink);
    text-align: right; padding-right: 14px; margin-top: 2px;
  }
  .testimonials__art { position: absolute; left: 0; top: 395px; width: 388px; height: 508px; }

  /* Studio photo with overlay */
  .studio {
    position: absolute; left: 412px; top: 12px; width: 778px; height: 521px;
    clip-path: polygon(0 0, 100% 0, 100% 465px, 394px 465px, 378px 100%, 0 100%);
  }
  .studio__photo { width: 100%; height: 100%;
    background: linear-gradient(135deg, #b9c93a 0%, #8a8f96 35%, #6e7078 55%, #8a6fb0 75%, #3c5aa8 100%); }
  .studio__note {
    position: absolute; left: 391px; top: 134px; width: 387px; height: 259px;
    background: var(--veil);
  }
  .studio__note::after {
    content: ""; position: absolute; left: 0; bottom: 0; width: 100%; height: 40px;
    background: var(--veil-band);
  }
  .studio__text {
    position: relative; z-index: 1; padding: 17px 90px 0 10px;
    font-family: "Open Sans", sans-serif; font-size: 13.4px; letter-spacing: 0.35px;
    line-height: 20.8px; color: var(--white);
  }

  /* Qualifications */
  .credentials {
    position: absolute; left: 412px; top: 545px; width: 377px; height: 287px;
    background: var(--sky);
  }
  .credentials__title {
    font-family: "Playfair Display SC", serif; font-weight: 700; color: var(--lemon);
    text-align: center; font-size: 30px; line-height: 31px; margin-top: 17px;
    text-shadow: 1px 2px 1px var(--lemon-shadow);
  }
  .credentials__title small { font-size: 24px; }
  .credentials__list {
    list-style: none; margin: 22px 0 0 24px;
    font-family: "PT Sans", sans-serif; font-weight: 700; font-size: 17.5px; color: var(--slate);
  }
  .credentials__list li { position: relative; padding-left: 14px; line-height: 30px; }
  .credentials__list li::before {
    content: ""; position: absolute; left: 0; top: 13px; width: 6px; height: 6px;
    border-radius: 50%; background: var(--bullet);
  }

  /* Brand bar */
  .brand {
    position: absolute; left: 412px; top: 836px; width: 377px; height: 79px;
    background: var(--logo-grey); border-radius: 0 0 10px 10px;
    display: flex; flex-direction: column; align-items: center; justify-content: center;
    font-family: "Open Sans", sans-serif; color: var(--ink); text-align: center;
  }
  .brand__name { font-weight: 700; font-size: 27px; line-height: 31px; }
  .brand__contact { font-size: 11.5px; line-height: 15px; }
  .brand__registry { font-size: 11px; line-height: 14px; }

  /* Trainer photo */
  .trainer {
    position: absolute; left: 801px; top: 492px; width: 389px; height: 423px;
    clip-path: polygon(36px 0, 100% 0, 100% 100%, 0 100%, 0 36px);
    background: linear-gradient(160deg, #e4ddd0 0%, #d9cfbe 50%, #cdbfa7 100%);
  }
  .specialties {
    position: absolute; left: 801px; top: 757px; width: 389px; height: 158px;
    background: var(--sand-veil); color: var(--white);
    font-family: "Open Sans", sans-serif; padding: 10px 14px 0 16px;
  }
  .specialties__motto { font-style: italic; font-weight: 600; font-size: 17px; line-height: 22px; }
  .specialties__heading { font-weight: 700; font-size: 13px; line-height: 18px; margin-top: 6px; }
  .specialties__list {
    list-style: decimal; columns: 2; column-gap: 14px; margin: 3px 0 0 18px;
    font-size: 12.5px; line-height: 17.5px;
  }
</style>
</head>
<body>
<main class="brochure">

  <section class="testimonials">
    <h2 class="testimonials__title">Testimonials</h2>
    <p class="quote quote--first">"My golf drive has increased dramatically from the use of sports specific exercises that Howard was able to deliver. The pain in my lower back has now ceased to flare up after a game"</p>
    <p class="quote__author">Colin</p>
    <p class="quote quote--second">&nbsp;"Howard's knowledge and application of exercise science and health has helped me achieve a stronger and leaner body in addition to improving my 5km walking time"</p>
    <p class="quote__author">Miriam</p>

    <svg class="testimonials__art" viewBox="0 0 388 508">
      <defs>
        <linearGradient id="torsoTone" x1="0" y1="0" x2="1" y2="1">
          <stop offset="0" stop-color="#c99a7c"/>
          <stop offset="0.55" stop-color="#a87658"/>
          <stop offset="1" stop-color="#6f6f72"/>
        </linearGradient>
      </defs>
      <path d="M388 0 C300 10 250 120 180 260 C120 380 60 470 0 508 L388 508 Z" fill="#ffffff"/>
      <path d="M388 10 C305 22 258 128 190 268 C132 386 72 478 14 508 L388 508 Z"
            fill="url(#torsoTone)" role="img" aria-label="Photo of a fit athlete's toned torso in grey track pants"/>
    </svg>
  </section>

  <section class="studio">
    <div class="studio__photo" role="img" aria-label="Photo of the home exercise studio with weight machines, racks and exercise balls"></div>
    <div class="studio__note">
      <p class="studio__text">I have an exercise studio with my home. It is literally the size of 6-7 x area of a standard bedroom.<br>Most importantly, it contains the latest state of the art exercise equipment (treamills, rowers, cycle &amp; recumberant bikes, elastic cords, bands, medballs, resistance machines, cables, squat racks, you name it..</p>
    </div>
  </section>

  <section class="credentials">
    <h2 class="credentials__title">Qualified Teacher<br><small>at your Service</small></h2>
    <ul class="credentials__list">
      <li>Certificate 4 personal trainer</li>
      <li>Diploma of fitness</li>
      <li>Bachelor of exercise and sport science</li>
      <li>Diploma of remedial massage</li>
      <li>First Aid certificate</li>
    </ul>
  </section>

  <footer class="brand">
    <span class="brand__name">Vigorhaven</span>
    <span class="brand__contact">0427 586 903 · hwtrelford@quillmail.com.au</span>
    <span class="brand__registry">Registered with Active Registry Australia</span>
  </footer>

  <div class="trainer" role="img" aria-label="Photo of the trainer sitting on a red exercise ball on a sandy beach"></div>

  <section class="specialties">
    <p class="specialties__motto">"Together, the sky is our limit"</p>
    <p class="specialties__heading">I specialize in:</p>
    <ol class="specialties__list">
      <li>Exercise rehabilitation</li>
      <li>Sport specific conditioning</li>
      <li>Functional strength</li>
      <li>Fat loss and toning</li>
      <li>Core strength &amp; stability</li>
      <li>Flexibility</li>
      <li>Cardio-respiratory fitness</li>
    </ol>
  </section>

</main>
</body>
</html>
```